Super Stunning and Creative 1-page Infographic Needed

Take the attached content and covert it into a 1-page 8.5x11" stunning, and highly engaging infographic. The infographic must:

* Use Birch Tool Supply colors
* Have icons and graphics used appropriately
* Look unique and creative, and super cool
* Be very eye catching

See attachment for content.

The topic is about retail inventory management. Retail = Store. Not warehouse looking. If you can add Birch Tool Supply photos, this may enhance it. Just a consideration, but not necessary.

Target Market(s)

Birch Tool Supply Store Owners

Industry/Entity Type

Retail Industry - Home Improvement

Font styles to use
Sans Serif

Requirements
Must have
• Birch Tool Supply Colors, Super Creative, Stunning and Eye Capturing. Graphics and icons where they make sense.
Should not have
• Common infographic look. It must look different.

```html
<!DOCTYPE html>
<html lang="en">
<head>
<meta charset="utf-8">
<title>8 Misconceptions About Managing Your Inventory Debunked</title>
<link href="https://fonts.googleapis.com/css2?family=Montserrat:wght@400;500;600;700;800&family=Poppins:wght@400;500;600;700&display=swap" rel="stylesheet">
<style>
:root{
  --red:#e3183b;
  --black:#111111;
  --white:#ffffff;
  --ink:#2a2a2a;
  --stage:#ececec;
}
*{box-sizing:border-box;margin:0;padding:0}
html,body{width:1200px;height:3293px;overflow:hidden;background:var(--stage)}
body{font-family:"Poppins",sans-serif;color:var(--ink)}
.sheet{position:absolute;left:50px;top:868px;width:1100px;height:1556px;background:var(--white);box-shadow:0 20px 50px rgba(0,0,0,.18);overflow:hidden}
.top-rule{position:absolute;left:0;top:0;width:100%;height:5px;background:var(--red)}
.top-band{position:absolute;right:0;top:0;width:350px;height:44px;background:var(--red);clip-path:polygon(0 0,100% 0,100% 100%,8% 100%)}
.header-bar{position:absolute;left:190px;top:78px;width:881px;height:118px;background:var(--black);border-radius:0 8px 8px 0}
.header-num{position:absolute;left:52px;top:58px;width:152px;height:152px;border-radius:50%;background:var(--red);border:6px solid var(--white);box-shadow:0 0 0 4px var(--red);display:flex;align-items:center;justify-content:center;font-family:"Montserrat",sans-serif;font-weight:800;font-size:140px;line-height:1;color:var(--white);z-index:2}
.header-title{position:absolute;left:237px;top:95px;font-family:"Montserrat",sans-serif;font-weight:700;font-size:39px;line-height:42px;text-transform:uppercase;z-index:2;white-space:nowrap}
.header-title .accent{color:var(--red);display:block}
.header-title .main{color:var(--white);display:block}
.myth{position:absolute;left:0;width:1100px;height:130px}
.myth-1{top:246px}.myth-2{top:360px}.myth-3{top:491px}.myth-4{top:631px}
.myth-5{top:754px}.myth-6{top:890px}.myth-7{top:1025px}.myth-8{top:1162px}
.hex{position:absolute;left:67px;top:-16px;width:96px;height:104px;z-index:2}
.hex svg{width:100%;height:100%}
.myth-bar{position:absolute;left:160px;top:0;width:854px;height:70px;border-radius:0 34px 34px 0;display:flex;align-items:center;padding:0 80px 0 23px;font-family:"Montserrat",sans-serif;font-weight:700;font-size:16.5px;line-height:20px;color:var(--white);text-transform:uppercase}
.myth-bar.red{background:var(--red)}
.myth-bar.black{background:var(--black)}
.myth-num{position:absolute;right:6px;top:11px;width:48px;height:48px;border-radius:50%;border:3px solid var(--white);display:flex;align-items:center;justify-content:center;font-family:"Montserrat",sans-serif;font-size:19px;font-weight:500;color:var(--white)}
.myth-body{position:absolute;left:183px;top:76px;width:832px;font-family:"Montserrat",sans-serif;font-size:13.5px;line-height:17px;color:var(--ink)}
.footnote{position:absolute;left:62px;top:1326px;font-family:"Poppins",sans-serif;font-weight:600;font-size:14.5px;color:var(--black);white-space:nowrap}
.pathway{position:absolute;left:62px;top:1364px;height:61px;display:flex;align-items:stretch}
.pathway-label{background:var(--red);color:var(--white);font-family:"Montserrat",sans-serif;font-weight:800;font-size:30px;display:flex;align-items:center;padding:0 20px;width:204px}
.crumb{background:var(--black);color:var(--white);font-family:"Poppins",sans-serif;font-size:17px;display:flex;align-items:center;padding:0 36px 0 40px;margin-left:-14px;clip-path:polygon(0 0,calc(100% - 22px) 0,100% 50%,calc(100% - 22px) 100%,0 100%,22px 50%)}
.footer{position:absolute;left:0;top:1453px;width:100%;height:63px}
.footer-stub{position:absolute;left:0;top:0;width:62px;height:63px;background:var(--black)}
.footer-brand{position:absolute;left:80px;top:0;height:63px;display:flex;align-items:center;gap:9px;font-family:"Montserrat",sans-serif;font-weight:800;font-size:20px;color:var(--red)}
.footer-brand .mark{width:13px;height:13px;background:var(--red)}
.footer-contact{position:absolute;left:330px;top:0;right:0;height:63px;background:var(--black);display:flex;align-items:center;gap:14px;padding-left:24px;font-family:"Poppins",sans-serif;font-size:23px;color:var(--white);white-space:nowrap}
.footer-contact svg{width:25px;height:25px;flex:none}
</style>
</head>
<body>
<main class="sheet">
  <div class="top-rule"></div>
  <div class="top-band"></div>

  <header>
    <div class="header-bar"></div>
    <div class="header-num">8</div>
    <h1 class="header-title"><span class="accent">Misconceptions About Managing</span><span class="main">Your Inventory Debunked</span></h1>
  </header>

  <section class="myths">
    <article class="myth myth-1">
      <div class="hex"><svg viewBox="0 0 96 104"><polygon points="48,2 93,27 93,77 48,102 3,77 3,27" fill="#111"/><g fill="#fff"><rect x="28" y="52" width="18" height="18"/><rect x="50" y="52" width="18" height="18"/><rect x="39" y="31" width="18" height="18"/></g></svg></div>
      <div class="myth-bar red">Getting my replenishment settings right is the most important way to manage inventory<span class="myth-num">01</span></div>
      <p class="myth-body">Maintaining strong inventory record accuracy (IRA) is the most critical factor toward staying in stock, addressing dead inventory, and driving incremental profitability.</p>
    </article>
    <article class="myth myth-2">
      <div class="hex"><svg viewBox="0 0 96 104"><polygon points="48,2 93,27 93,77 48,102 3,77 3,27" fill="#111"/><circle cx="48" cy="52" r="21" fill="none" stroke="#fff" stroke-width="5" stroke-dasharray="8 3"/><g stroke="#fff" stroke-width="4" fill="none"><line x1="39" y1="61" x2="57" y2="43"/><circle cx="40" cy="44" r="3"/><circle cx="56" cy="60" r="3"/></g></svg></div>
      <div class="myth-bar black">When sales have slowed, inventory needs cutting<span class="myth-num">02</span></div>
      <p class="myth-body">Efforts to reduce inventory can be lethal, creating out of stocks, empty shelves, poor store image perception, and frustrated customers who will ultimately shop the competition. Instead, if inventories need to be reduced, prioritize by looking at unproductive products taking a more strategic approach to healthier inventory levels.</p>
    </article>
    <article class="myth myth-3">
      <div class="hex"><svg viewBox="0 0 96 104"><polygon points="48,2 93,27 93,77 48,102 3,77 3,27" fill="#111"/><g fill="#fff"><rect x="28" y="58" width="9" height="14"/><rect x="41" y="50" width="9" height="22"/><rect x="54" y="42" width="9" height="30"/></g><polyline points="26,52 40,40 50,46 68,30" fill="none" stroke="#fff" stroke-width="4"/><polygon points="70,28 60,29 69,38" fill="#fff"/></svg></div>
      <div class="myth-bar red">Dead stock (stuff that hasn’t sold in years) needs to be marked down and moved out<span class="myth-num">03</span></div>
      <p class="myth-body">Leverage markdowns as a last resort. Instead, first check to see if the product is even physically in the store, priced competitively, redundant product in the set, or merchandised effectively. More times than not you can move product without having to sell it at a discount.</p>
    </article>
    <article class="myth myth-4">
      <div class="hex"><svg viewBox="0 0 96 104"><polygon points="48,2 93,27 93,77 48,102 3,77 3,27" fill="#111"/><g fill="none" stroke="#fff" stroke-width="4" stroke-linecap="round"><path d="M48 56 V38"/><path d="M48 44 C40 44 36 38 36 32 C44 32 48 36 48 44Z" fill="#fff"/><path d="M48 40 C56 40 60 34 60 28 C52 28 48 32 48 40Z" fill="#fff"/><path d="M26 66 L38 60 H54 L58 64 H46"/><path d="M58 64 L70 56"/></g></svg></div>
      <div class="myth-bar red">Working my mango count sheets will drive sustainable improvements to IRA<span class="myth-num">04</span></div>
      <p class="myth-body">Maintaining strong inventory record accuracy (IRA) is the most critical factor toward staying in stock, addressing dead inventory, and driving incremental profitability.</p>
    </article>
    <article class="myth myth-5">
      <div class="hex"><svg viewBox="0 0 96 104"><polygon points="48,2 93,27 93,77 48,102 3,77 3,27" fill="#111"/><g fill="none" stroke="#fff" stroke-width="4"><circle cx="48" cy="52" r="20"/><path d="M30 46 C38 46 40 54 46 56 C50 58 48 66 46 72"/><path d="M56 34 C54 40 60 44 66 44"/><path d="M24 36 A28 28 0 0 1 60 26"/></g></svg></div>
      <div class="myth-bar black">Increasing my inventory depth will hurt profits and drive down my inventory turns<span class="myth-num">05</span></div>
      <p class="myth-body">Stores who have deeper levels of inventory outperform stores that don’t. When focused on raising inventory strategically through programs like economic order quantities, minimum order points, and preseason planner, inventory turns typically remain the same as inventory increases.</p>
    </article>
    <article class="myth myth-6">
      <div class="hex"><svg viewBox="0 0 96 104"><polygon points="48,2 93,27 93,77 48,102 3,77 3,27" fill="#111"/><g fill="none" stroke="#fff" stroke-width="4"><rect x="28" y="40" width="40" height="28" rx="3"/><path d="M40 40 V34 H56 V40"/><path d="M28 52 H68"/></g></svg></div>
      <div class="myth-bar red">Spending more than an hour (or more) working the ‘RSO’ will result in better quality suggested orders<span class="myth-num">06</span></div>
      <p class="myth-body">Typically, if it takes greater than 60 minutes to work your RSO each week per store, there are larger issues at play. The goal is to be able to review the RSO on an exception basis for outliers and transmit it through to then shift focus on other important store activities.</p>
    </article>
    <article class="myth myth-7">
      <div class="hex"><svg viewBox="0 0 96 104"><polygon points="48,2 93,27 93,77 48,102 3,77 3,27" fill="#111"/><g fill="none" stroke="#fff" stroke-width="5"><path d="M32 66 A22 22 0 1 1 64 66" stroke-dasharray="9 4"/><line x1="48" y1="54" x2="58" y2="40" stroke-linecap="round"/></g><circle cx="48" cy="54" r="5" fill="#fff"/></svg></div>
      <div class="myth-bar black">Carry more weeks of supply on fast moving products and less on slower velocity SKUs<span class="myth-num">07</span></div>
      <p class="myth-body">Based on how Ledger POS calculates order points, this can result in overstocking on faster goods and insufficient amounts of slower ones. Revisit your weeks of supply settings to ensure they are maintained at or near Birch best practice levels.</p>
    </article>
    <article class="myth myth-8">
      <div class="hex"><svg viewBox="0 0 96 104"><polygon points="48,2 93,27 93,77 48,102 3,77 3,27" fill="#111"/><g fill="none" stroke="#fff" stroke-width="4" stroke-linejoin="round"><polygon points="48,30 68,41 68,63 48,74 28,63 28,41"/><polyline points="28,41 48,52 68,41"/><line x1="48" y1="52" x2="48" y2="74"/></g></svg></div>
      <div class="myth-bar red">With the onset of global supply chain issues, reaching a 95% in-stock position is next to impossible<span class="myth-num">08</span></div>
      <p class="myth-body">Undoubtably, the industry supply problems make obtaining a higher in-stock position more challenging, but still quite probable. The key is to focus on what you are able to control within the four walls of your operations and consistently execute the basics (i.e. count sheets, shooting the outs, item change management).</p>
    </article>
  </section>

  <p class="footnote">See the Birch Way of Retailing Inventory Management section for further insights and practices to optimize inventory health</p>

  <nav class="pathway">
    <span class="pathway-label">PATHWAY:</span>
    <span class="crumb">BIRCHNET</span>
    <span class="crumb">About Birch</span>
    <span class="crumb">Birch Way of Retailing</span>
    <span class="crumb">Inventory Management</span>
  </nav>

  <footer class="footer">
    <div class="footer-stub"></div>
    <div class="footer-brand"><span class="mark"></span>BIRCH TOOL SUPPLY</div>
    <div class="footer-contact">
      <svg viewBox="0 0 24 24"><path d="M6.6 10.8a15.1 15.1 0 0 0 6.6 6.6l2.2-2.2a1 1 0 0 1 1-.25 11.4 11.4 0 0 0 3.6.57 1 1 0 0 1 1 1V20a1 1 0 0 1-1 1A17 17 0 0 1 3 4a1 1 0 0 1 1-1h3.5a1 1 0 0 1 1 1c0 1.250.2 2.45.57 3.6a1 1 0 0 1-.25 1z" fill="#fff"/></svg>
      <span>555.014.2290</span>
      <svg viewBox="0 0 24 24"><rect x="2" y="5" width="20" height="14" rx="2" fill="none" stroke="#fff" stroke-width="2"/><polyline points="2,6 12,13 22,6" fill="none" stroke="#fff" stroke-width="2"/></svg>
      <span>StoreOperations@birchtoolsupply.com</span>
    </div>
  </footer>
</main>
</body>
</html>
```